Redesign Website

I currently have a website www.quillbrookrehab.com that I would like to have redesigned for esthetics and design limitations with the present platform. I will provide my logo, background logo (attached) , current site, foundation grip PSD.zip (attached) and a questionnaire (attached) from a web design company to provide the input to have an impressive site that pleases the eyes and makes an impact. I would also like the site to be mobile friendly.

IMPORTANT:
- The final PSD must include:
o Homepage Mockup
o Internal Pages Mockup
o Mobile site mockup
o Fonts files used in mockup

Final website will be responsive, using the Foundation Framework. Attached you will find a PSD of the Foundation grid – please use this and include with your final PSD. Here is a link for reference:
http://plenvix.com/article/1053/foundation-s-grid-and-photoshop-what-you-

Target Market(s)

Patients for physical therapy

Industry/Entity Type

It Company

Requirements
Must have
• Pages included in the present site. Photos and design should change.
Nice to have
• Should provide information necessary for patients to schedule an appointment
Should not have
• Should not be difficult to read.

```html
<!DOCTYPE html>
<html lang="en">
<head>
<meta charset="utf-8">
<title>Quillbrook Sports &amp; Orthopedic Physical Therapy</title>
<link href="https://fonts.googleapis.com/css2?family=Open+Sans:ital,wght@0,400;0,600;0,700;1,400&family=Roboto+Condensed:wght@700&display=swap" rel="stylesheet">
<style>
:root{
  --red:#c8102e;
  --red-dark:#a50d25;
  --green:#6db33f;
  --ink:#333;
  --muted:#666;
  --light:#999;
  --panel:#f2f2f2;
  --line:#dcdcdc;
  --white:#fff;
}
*{box-sizing:border-box;margin:0;padding:0}
html,body{width:1200px;height:2398px;overflow:hidden;background:var(--white);font-family:"Open Sans",Arial,sans-serif;color:var(--ink)}
.page{position:relative;width:1200px;height:2398px}
.abs{position:absolute}

/* header */
.brand{left:195px;top:12px;display:flex;align-items:center;gap:12px;color:var(--red);font-weight:700}
.brand-mark{width:56px;height:56px;border-radius:50%;background:var(--red)}
.brand-name{font-size:30px;line-height:1}
.brand-sub{font-size:12px;line-height:1.3;letter-spacing:.5px}
.top-contact{right:220px;top:30px;font-size:13px;color:var(--muted);text-align:right;line-height:24px}
.nav{left:0;top:86px;width:1200px;height:39px;background:linear-gradient(var(--red),var(--red-dark))}
.nav ul{list-style:none;display:flex;justify-content:space-between;position:absolute;left:216px;top:11px;width:768px}
.nav li{color:var(--white);font-family:"Roboto Condensed",Arial,sans-serif;font-size:12.5px;font-weight:700;text-transform:uppercase;white-space:nowrap;line-height:17px}

/* hero */
.hero{left:0;top:125px;width:1200px;height:503px;background:linear-gradient(100deg,#5e7f84 0%,#8aa5a0 30%,#3b4e6a 55%,#c0bfd0 80%,#6f7fa0 100%)}
.hero-title{left:242px;top:305px;font-family:"Roboto Condensed",Arial,sans-serif;font-weight:700;font-size:42px;color:var(--white);line-height:1}
.hero-sub{left:242px;top:350px;font-size:38px;color:var(--white);line-height:1.2}
.hero-text{left:242px;top:402px;font-size:14px;color:var(--white);width:300px;line-height:20px}
.btn-red{left:242px;top:462px;width:186px;height:32px;background:var(--red);color:var(--white);font-size:13px;font-weight:700;text-align:center;line-height:32px}
.dots{left:582px;top:605px;display:flex;gap:4px}
.dots span{width:10px;height:10px;border-radius:50%;background:var(--white)}
.dots span:nth-child(1){background:var(--red)}
.dots span:nth-child(2){background:#e8c21a}

/* social */
.social{left:258px;top:648px;display:flex;gap:20px}
.social span{width:32px;height:32px;border-radius:50%;background:#d4d4d4}
.social span.accent{background:var(--red)}
.call{left:660px;top:642px;height:44px;border-left:1px solid var(--line);padding-left:20px;font-size:19px;color:var(--muted);line-height:44px;white-space:nowrap}
.call b{color:var(--green);font-weight:400;font-size:23px}
.rule{left:0;top:705px;width:1200px;height:1px;background:#ececec}

.welcome{left:0;top:740px;width:1200px;text-align:center;font-size:27px;font-weight:400;color:#444;white-space:nowrap}
.welcome span{color:var(--red)}
.welcome-text{left:240px;top:826px;width:720px;text-align:center;font-size:10px;line-height:15px;color:var(--muted)}

/* professionals */
.pros{left:0;top:915px;width:1200px;height:390px;background:var(--panel)}
.h2{font-size:23px;color:var(--red);font-weight:400;white-space:nowrap}
.pro-photo{left:230px;top:968px;width:360px;height:302px;background:radial-gradient(circle at 50% 45%,#d9b8a4 0,#a9b9d1 45%,#eef0f3 75%)}
.pro-name{left:612px;top:976px;font-size:17px;color:#444}
.pro-bio{left:612px;top:1004px;width:350px;font-size:9.5px;line-height:14.5px;color:var(--muted)}

/* services */
.svc-img{top:1383px;width:166px;height:135px}
.svc-list{top:1534px;font-size:11px;line-height:19px;color:#444;width:172px}
.svc-list .nw{white-space:nowrap}
.more{color:var(--green);font-size:10px}

/* testimonials */
.quote{font-size:10.5px;line-height:16px;color:var(--muted);font-style:italic;width:340px}
.avatar{width:92px;height:92px;border-radius:50%;border:3px solid var(--line)}
.who{font-size:10.5px;color:var(--muted)}
.who b{color:var(--green);font-weight:600}
.read-bar{left:242px;top:1992px;width:456px;height:28px;background:#eaeaea;font-size:11.5px;line-height:28px;padding-left:14px;color:#444}

/* appointment */
.appt{left:722px;top:1695px;width:236px;height:350px;background:var(--panel)}
.appt h3{position:absolute;left:24px;top:16px;font-size:19px;color:var(--red);font-weight:400;white-space:nowrap}
.field{position:absolute;left:24px;width:188px;height:26px;background:var(--white);border:1px solid var(--line);font-size:10.5px;color:var(--light);line-height:24px;padding-left:8px}
.submit{position:absolute;left:24px;top:264px;width:188px;height:32px;background:var(--green);color:var(--white);font-size:13px;text-align:center;line-height:32px}

/* footer */
.footer{left:0;top:2055px;width:1200px;height:343px;background:var(--panel)}
.fh{font-size:14px;color:#444;font-weight:600}
.ft{font-size:9.5px;line-height:14px;color:var(--muted)}
.ft .time{color:var(--red)}
.thumb{width:42px;height:42px;background:var(--white);border:1px solid var(--line)}
.btn-green{background:var(--green);color:var(--white);font-size:11px;text-align:center}
.foot-rule{left:242px;top:2318px;width:716px;height:1px;background:var(--line)}
.copy{left:242px;top:2335px;font-size:9.6px;color:var(--muted)}
.foot-links{left:660px;top:2333px;display:flex;font-size:10px;color:var(--muted)}
.foot-links span{padding:0 20px;border-left:1px solid var(--line)}
.foot-links span:first-child{border-left:0}
</style>
</head>
<body>
<div class="page">

  <header>
    <div class="abs brand">
      <span class="brand-mark"></span>
      <div>
        <div class="brand-name">Quillbrook</div>
        <div class="brand-sub">SPORTS &amp; ORTHOPEDIC<br>PHYSICAL THERAPY</div>
      </div>
    </div>
    <div class="abs top-contact">FREE Consultation : 610.555.0142<br>Appointment &nbsp;|&nbsp; Register</div>
    <nav class="abs nav">
      <ul>
        <li>Home</li><li>Location</li><li>Hours</li><li>Our Story</li><li>Mission Statement</li><li>Services</li><li>Insurance</li><li>New Patients</li><li>Contact Us</li><li>Testimonials</li><li>Community</li>
      </ul>
    </nav>
  </header>

  <section>
    <div class="abs hero" role="img" aria-label="Therapist stretching the leg of a patient lying on a treatment table in a clinic"></div>
    <div class="abs hero-title">SPORTS MEDICINE</div>
    <div class="abs hero-sub">Rehabilitation</div>
    <div class="abs hero-text">Lorem Ipsum is simply dummy content of the text of the printing</div>
    <div class="abs btn-red">REGISTER NOW</div>
    <div class="abs dots"><span></span><span></span><span></span></div>
  </section>

  <div class="abs social"><span></span><span></span><span></span><span></span><span></span><span></span><span></span><span class="accent"></span></div>
  <div class="abs call">Call Now Free : <b>610.555.0142</b></div>
  <div class="abs rule"></div>

  <h1 class="abs welcome">Welcome to awesome <span>Quillbrook Sports &amp; Orthopedic Physical Therapy</span></h1>
  <p class="abs welcome-text">Lorem ipsum dolor sit amet, consectetur adipiscing elit. Vestibulum sodales, magna et mattis placerat, dui velit semper lacus, quis facilisis arcu est at eros. Mauris sed ultrices mauris. Curabitur et quam justo, vitae luctus ligula. Vestibulum volutpat sapien accumsan mi dignissim dictum.</p>

  <section>
    <div class="abs pros"></div>
    <h2 class="abs h2" style="left:242px;top:922px">Our professionals</h2>
    <div class="abs pro-photo" role="img" aria-label="Portrait of the lead physical therapist in a blue shirt"></div>
    <div class="abs pro-name">Mark Delaney, PT, DPT, MS</div>
    <p class="abs pro-bio">Our services are the culmination of 15 years of experience of Dr. Mark Delaney, PT, DPT, MS in the sports and orthopedic physical therapy arena. Mark directed the rehabilitation services for the largest orthopedic group in Brookfield County, working with specialists in spine, shoulder, elbow, wrist, hand, hip, knee, ankle and foot surgery. His expertise is the treatment of all sports and orthopedic injuries, whether they are the result of trauma, repetitive movements or postures, or a surgical intervention. Mark is confident that his knowledge base and manual skills will make Quillbrook a keystone in the private practice physical therapy community. Quillbrook is a direct extension of his commitment to be an integral health care provider, with an atmosphere conducive to rehabilitation for clients from adolescents to geriatrics. Come in or correspond with our office. You will see that we value you as a client and would like to make you part of our community! If you have questions about your injury and treatment, please contact us and know you have a partner you can trust.</p>
  </section>

  <section>
    <h2 class="abs h2" style="left:242px;top:1334px">Our Services</h2>
    <div class="abs svc-img" style="left:242px;background:linear-gradient(135deg,#e8e6e3,#4b4b4f)" role="img" aria-label="Knee brace being fitted on an athlete's leg"></div>
    <div class="abs svc-img" style="left:425px;background:linear-gradient(135deg,#a9c3dc,#5b7fa8)" role="img" aria-label="Surgeons in blue scrubs in an operating room"></div>
    <div class="abs svc-img" style="left:610px;background:linear-gradient(160deg,#d84a3a,#3f7a3a)" role="img" aria-label="Soccer players competing for the ball on a field"></div>
    <div class="abs svc-img" style="left:792px;background:linear-gradient(135deg,#8a7565,#3a3a3a)" role="img" aria-label="Runner's feet on a track"></div>
    <div class="abs svc-list" style="left:242px"><span class="nw">Sports Medicine rehabilitation</span><br><span class="nw">Orthopedic Injury rehabilitation</span><br>Post fracture rehabilitation<br><span class="more">read more</span></div>
    <div class="abs svc-list" style="left:425px">Preoperative rehabilitation<br>Postoperative rehabilitation<br>Spine rehabilitation<br><span class="more">read more</span></div>
    <div class="abs svc-list" style="left:610px;line-height:15px">ACL prehab (lower extremity injury prevention program)<br><span class="nw" style="display:inline-block;margin:4px 0">Balance &amp; Proprioception training</span><br>Neurological rehabilitation<br><span style="display:inline-block;margin-top:4px">Hand and Upper extremity rehabilitation</span><br><span class="more">read more</span></div>
    <div class="abs svc-list" style="left:792px">Gait Analysis<br>Running Analysis<br><span class="more">read more</span></div>
  </section>

  <section>
    <h2 class="abs h2" style="left:242px;top:1710px">What our patients say</h2>
    <div class="abs avatar" style="left:242px;top:1755px;background:linear-gradient(#c98a6a,#e9d6cc)" role="img" aria-label="Patient portrait"></div>
    <p class="abs quote" style="left:350px;top:1768px">If you are looking for a Physical Therapist go see Mark. He is very good at what he does. He has a great sense of humor which is needed to get thru PT.</p>
    <div class="abs who" style="left:350px;top:1822px"><b>Dana</b>, CEO</div>
    <div class="abs avatar" style="left:242px;top:1868px;background:linear-gradient(#b58f78,#e3ddd8)" role="img" aria-label="Patient portrait"></div>
    <p class="abs quote" style="left:350px;top:1884px">Mark did a fantastic job guiding me through shoulder surgery rehab! His knowledge and experience are certainly assets for Quillbrook.</p>
    <div class="abs who" style="left:350px;top:1936px"><b>Colin</b>, MD</div>
    <div class="abs read-bar">Read more what patients say</div>

    <form class="abs appt">
      <h3>Make an Appointment</h3>
      <div class="field" style="top:62px">Full Name</div>
      <div class="field" style="top:94px">Phone Number</div>
      <div class="field" style="top:126px">Email Address</div>
      <div class="field" style="top:158px">Appointment Date
        <svg width="12" height="12" style="position:absolute;right:8px;top:6px"><rect x="0.5" y="1.5" width="11" height="10" fill="none" stroke="#999"/><line x1="0" y1="4.5" x2="12" y2="4.5" stroke="#999"/></svg>
      </div>
      <div class="field" style="top:190px;height:64px;line-height:22px">Message</div>
      <div class="submit">Submit Request</div>
    </form>
  </section>

  <footer>
    <div class="abs footer"></div>
    <div class="abs fh" style="left:246px;top:2096px">Text blurb</div>
    <p class="abs ft" style="left:246px;top:2122px;width:150px">Lorem ipsum dolor sit malesuada adipiscing elit. Maecenas ac sagittis est. Duis magna odio, sollicitudin in porta ac, ornare a dui.<br><br>Sollicitudin in porta ac, ornare a dui. Nulla auctor ante.</p>
    <div class="abs btn-green" style="left:246px;top:2250px;width:76px;height:24px;line-height:24px">Read More</div>

    <div class="abs fh" style="left:428px;top:2096px">Latest Tweets</div>
    <p class="abs ft" style="left:428px;top:2122px;width:150px">@Quillbrook Sports &amp; Orthopedic. Contrary to popular belief, Lorem ipsum is not simply random text.<br><span class="time">25 minute ago</span><br><br>Quillbrook Sports &amp; Orthopedic. Contrary to popular belief, Lorem ipsum is not simply random text.<br><span class="time">25 minute ago</span></p>

    <div class="abs fh" style="left:607px;top:2096px">Photo Stream</div>
    <div class="abs thumb" style="left:607px;top:2126px"></div>
    <div class="abs thumb" style="left:657px;top:2126px"></div>
    <div class="abs thumb" style="left:707px;top:2126px"></div>
    <div class="abs thumb" style="left:607px;top:2184px"></div>
    <div class="abs thumb" style="left:657px;top:2184px"></div>
    <div class="abs thumb" style="left:707px;top:2184px"></div>

    <div class="abs fh" style="left:788px;top:2096px">Newsletter signup</div>
    <p class="abs ft" style="left:788px;top:2122px;width:150px">Sign up our newsletter to get latest updates.</p>
    <div class="abs field" style="left:788px;top:2167px;width:136px;height:28px;font-size:8px">Email Address</div>
    <div class="abs btn-green" style="left:924px;top:2167px;width:30px;height:28px;line-height:28px">GO</div>

    <div class="abs foot-rule"></div>
    <div class="abs copy">Quillbrook Sports &amp; Orthopedic Physical Therapy © 2013 All Rights Reserved.</div>
    <div class="abs foot-links"><span>Links</span><span>Links</span><span>Links</span><span>Links</span><span>Links</span></div>
  </footer>

</div>
</body>
</html>
```